Business Card Design for Irrigation Contractor

Design and layout for company business cards to include the following information:
1. Logo
2. Installation \ Service \ Maintenance
3. U-47326
4. Walter K. Lindqvist
5. walter@kelvaspray.com
6. Office 561-738-2196
7. Cell 561-629-8513

```html
<!DOCTYPE html>
<html lang="en">
<head>
<meta charset="utf-8">
<title>Kelva Spray – Business Card</title>
<link rel="stylesheet" href="https://fonts.googleapis.com/css2?family=Montserrat:wght@500;600;700;800&display=swap">
<style>
  :root {
    --page-bg: #ebe8e3;
    --card-bg: #ffffff;
    --navy: #1c3a66;
    --ink: #1b2b45;
    --blue: #2f80c8;
    --sky: #5bb6e8;
    --deep: #1f5d9e;
    --shadow: rgba(40, 30, 20, 0.28);
  }
  * { box-sizing: border-box; margin: 0; padding: 0; }
  html, body {
    width: 900px; height: 1200px; overflow: hidden;
    background: var(--page-bg);
    font-family: "Montserrat", sans-serif;
  }
  .canvas { position: relative; width: 900px; height: 1200px; }
  .card {
    position: absolute; left: 87px; width: 733px; height: 430px;
    background: var(--card-bg); border-radius: 22px; overflow: hidden;
    box-shadow: 0 6px 18px var(--shadow);
  }
  .card--front { top: 125px; }
  .card--back { top: 640px; }

  .brand-name {
    font-weight: 800; color: var(--navy); letter-spacing: 0.5px;
    text-transform: uppercase; line-height: 1;
  }
  .brand-tagline {
    font-weight: 600; color: var(--blue); text-transform: uppercase;
    letter-spacing: 0.6px; line-height: 1;
  }

  .front-brand { position: absolute; left: 41px; top: 70px; }
  .front-brand .brand-name { font-size: 35px; }
  .front-brand .brand-tagline { font-size: 12.5px; margin-top: 8px; }

  .contact { position: absolute; left: 41px; top: 240px; color: var(--ink); }
  .contact-name {
    font-size: 18.5px; font-weight: 700; text-transform: uppercase;
    letter-spacing: 0.4px; color: var(--navy); margin-bottom: 14px;
  }
  .contact-list { list-style: none; }
  .contact-item {
    display: flex; align-items: center; gap: 7px;
    font-size: 16px; font-weight: 500; height: 29px;
  }
  .contact-item svg { width: 16px; height: 16px; fill: var(--deep); flex: none; }
  .license { font-size: 14px; font-weight: 500; margin-top: 16px; }

  .front-mark { position: absolute; left: 400px; top: 0; width: 333px; height: 430px; }

  .back-brand {
    position: absolute; left: 0; right: 0; top: 95px;
    display: flex; flex-direction: column; align-items: center;
  }
  .back-brand .brand-dot {
    width: 70px; height: 70px; border-radius: 50%;
    background: linear-gradient(160deg, var(--sky), var(--deep));
    margin-bottom: 62px;
  }
  .back-brand .brand-name { font-size: 40px; }
  .back-brand .brand-tagline { font-size: 15px; margin-top: 9px; }
</style>
</head>
<body>
<main class="canvas">

  <section class="card card--front">
    <header class="front-brand">
      <div class="brand-name">Kelva Spray</div>
      <div class="brand-tagline">Installation • Service • Maintenance</div>
    </header>

    <div class="contact">
      <div class="contact-name">Walter K. Lindqvist</div>
      <ul class="contact-list">
        <li class="contact-item">
          <svg viewBox="0 0 24 24" aria-hidden="true"><path d="M6.6 10.8a15.5 15.5 0 0 0 6.6 6.6l2.2-2.2c.3-.3.7-.4 1-.2 1.1.4 2.3.6 3.6.6.6 0 1 .4 1 1V20c0 .6-.4 1-1 1A17 17 0 0 1 3 4c0-.6.4-1 1-1h3.5c.6 0 1 .4 1 1 0 1.3.2 2.5.6 3.6.1.3 0 .7-.2 1z"/></svg>
          <span>561-738-2196</span>
        </li>
        <li class="contact-item">
          <svg viewBox="0 0 24 24" aria-hidden="true"><path d="M7 2h10a2 2 0 0 1 2 2v16a2 2 0 0 1-2 2H7a2 2 0 0 1-2-2V4a2 2 0 0 1 2-2zm0 3v13h10V5zm5 14.2a1 1 0 1 0 0 2 1 1 0 0 0 0-2z"/></svg>
          <span>561-629-8513</span>
        </li>
        <li class="contact-item">
          <svg viewBox="0 0 24 24" aria-hidden="true"><path d="M2 6h20v12H2zm2 1.5v.3l8 5.2 8-5.2v-.3zm0 2.4V16.5h16V9.9l-8 5.2z"/></svg>
          <span>walter@kelvaspray.com</span>
        </li>
      </ul>
      <div class="license">U-47326</div>
    </div>

    <svg class="front-mark" viewBox="0 0 333 430" role="img" aria-label="Large brand emblem area in blue tones">
      <defs>
        <linearGradient id="markFill" x1="0" y1="0" x2="1" y2="1">
          <stop offset="0" stop-color="#5bb6e8"/>
          <stop offset="1" stop-color="#1f5d9e"/>
        </linearGradient>
      </defs>
      <circle cx="250" cy="300" r="140" fill="url(#markFill)"/>
    </svg>
  </section>

  <section class="card card--back">
    <div class="back-brand">
      <div class="brand-dot" aria-hidden="true"></div>
      <div class="brand-name">Kelva Spray</div>
      <div class="brand-tagline">Installation • Service • Maintenance</div>
    </div>
  </section>

</main>
</body>
</html>
```